Label Design for Nuts package*

Develop the design for a label for nuts sold in a paperbag.

you can find our website here: www.kornfeld-snack.de.
Here comes the link to our catalogue: https://www.blattwerk-docs.com/de/document/read/48172956/kornfeld-premium-snacks-gesamtkatalog-2019

With this product we are targeting private customers who want to buy nuts with plastic free packaging online.
The colours of the label should fit the brown paper bag.

```html
<!DOCTYPE html>
<html lang="en">
<head>
<meta charset="utf-8">
<title>Kornfeld Premium Snacks – Nut Label Concepts</title>
<link href="https://fonts.googleapis.com/css2?family=Comfortaa:wght@300&family=Questrial&family=Marcellus&family=Cinzel:wght@400&display=swap" rel="stylesheet">
<style>
  :root {
    --kraft: #e4d4b9;
    --kraft-dark: #d9c6a6;
    --orange: #f0853f;
    --orange-bar: #d28744;
    --brown: #8b3a1d;
    --white: #ffffff;
    --ink: #3a2a1e;
    --almond-light: #d69a5e;
    --almond-mid: #b9773f;
    --almond-dark: #7d4a24;
    --frame: #9a9a9a;
  }
  * { margin: 0; padding: 0; box-sizing: border-box; }
  html, body { width: 1200px; height: 707px; overflow: hidden; background: var(--white); }
  .sheet {
    position: relative; width: 1200px; height: 707px;
    background: var(--white); border: 1px solid var(--frame);
  }
  .bag {
    position: absolute; top: 34px; height: 644px;
    background: radial-gradient(ellipse at 40% 30%, var(--kraft) 0%, var(--kraft-dark) 100%);
    border: 1px solid #6f6f6f;
    overflow: hidden;
  }
  .bag--classic { left: 42px; width: 338px; }
  .bag--framed { left: 424px; width: 361px; }
  .bag--modern { left: 806px; width: 364px; }
  .shape { position: absolute; display: block; }
  .product-window {
    position: absolute;
    background: radial-gradient(circle at 35% 35%, var(--almond-light), var(--almond-mid) 55%, var(--almond-dark));
  }
  .brand {
    position: absolute; left: 0; right: 0; text-align: center;
    font-family: 'Comfortaa', sans-serif; font-weight: 300;
  }
  .brand__mark {
    display: block; margin: 0 auto 10px; width: 40px; height: 40px; border-radius: 50%;
  }
  .brand__name { display: block; font-size: 40px; letter-spacing: 2px; line-height: 1; }
  .brand__tagline {
    display: inline-block; margin-top: 8px; padding: 0 6px 4px;
    font-family: 'Cinzel', serif; font-size: 11px; letter-spacing: 2.5px;
    border-bottom: 1px solid currentColor;
  }
  .product-name {
    position: absolute; font-family: 'Questrial', sans-serif; letter-spacing: 3px; line-height: 1;
  }

  /* classic */
  .bag--classic .shape { left: 42px; top: 48px; }
  .bag--classic .brand { top: 92px; color: var(--white); left: 42px; right: 22px; }
  .bag--classic .brand__mark { background: var(--white); }
  .bag--classic .nuts-band {
    position: absolute; left: 42px; top: 288px; width: 272px; height: 38px;
    background: var(--brown);
    border-top: 3px double var(--orange); border-bottom: 3px double var(--orange);
  }
  .bag--classic .product-name {
    left: 0; right: 0; top: 3px; text-align: center; font-size: 28px; color: var(--white);
  }
  .bag--classic .product-window { left: 56px; top: 328px; width: 244px; height: 240px; }

  /* framed */
  .bag--framed .shape { left: 34px; top: -1px; }
  .bag--framed .brand { top: 52px; left: 70px; width: 222px; color: var(--brown); }
  .bag--framed .brand__mark { background: var(--brown); width: 36px; height: 36px; }
  .bag--framed .brand__name { font-size: 34px; }
  .bag--framed .product-name {
    left: 34px; width: 292px; top: 206px; text-align: center; font-size: 27px; color: var(--white);
  }
  .bag--framed .product-window { left: 58px; top: 326px; width: 243px; height: 242px; }

  /* modern */
  .bag--modern .nuts-bar {
    position: absolute; left: 0; top: 303px; width: 316px; height: 45px; background: var(--orange-bar);
  }
  .bag--modern .product-name {
    left: 42px; top: 7px; font-family: 'Marcellus', serif; font-size: 34px; letter-spacing: 0; color: var(--ink);
  }
  .bag--modern .product-window {
    left: 45px; top: 350px; width: 318px; height: 204px;
    background: radial-gradient(circle at 40% 40%, #d98a4a, #b86a30 60%, #8a4a20);
  }
  .bag--modern .brand { top: 386px; left: 45px; width: 318px; color: var(--white); }
  .bag--modern .brand__mark { background: var(--white); width: 36px; height: 36px; }
  .bag--modern .brand__name { font-size: 34px; }
  .bag--modern .accent-block {
    position: absolute; left: 262px; top: 554px; width: 101px; height: 26px; background: var(--orange);
  }
</style>
</head>
<body>
<main class="sheet">

  <section class="bag bag--classic" aria-label="Label concept one">
    <svg class="shape" width="272" height="552" viewBox="0 0 272 552" aria-hidden="true">
      <path d="M14,0 H258 A14 14 0 0 0 272,14 V538 A14 14 0 0 0 258,552 H14 A14 14 0 0 0 0,538 V14 A14 14 0 0 0 14,0 Z" fill="var(--orange)"/>
    </svg>
    <div class="brand">
      <span class="brand__mark"></span>
      <span class="brand__name">kornfeld</span>
      <span class="brand__tagline">PREMIUM SNACKS</span>
    </div>
    <div class="nuts-band"><span class="product-name">NUTS</span></div>
    <div class="product-window" role="img" aria-label="Photo of shelled almonds"></div>
  </section>

  <section class="bag bag--framed" aria-label="Label concept two">
    <svg class="shape" width="292" height="256" viewBox="0 0 292 256" aria-hidden="true">
      <path d="M0,0 H292 V236 A16 16 0 0 0 276,252 Q146,228 16,252 A16 16 0 0 0 0,236 Z" fill="var(--brown)"/>
      <rect x="36" y="0" width="222" height="196" fill="var(--white)"/>
    </svg>
    <div class="brand">
      <span class="brand__mark"></span>
      <span class="brand__name">kornfeld</span>
      <span class="brand__tagline">PREMIUM SNACKS</span>
    </div>
    <span class="product-name">NUTS</span>
    <div class="product-window" role="img" aria-label="Photo of shelled almonds"></div>
  </section>

  <section class="bag bag--modern" aria-label="Label concept three">
    <div class="nuts-bar"><span class="product-name">NUTS</span></div>
    <div class="product-window" role="img" aria-label="Close-up photo of almonds"></div>
    <div class="brand">
      <span class="brand__mark"></span>
      <span class="brand__name">kornfeld</span>
      <span class="brand__tagline">PREMIUM SNACKS</span>
    </div>
    <div class="accent-block"></div>
  </section>

</main>
</body>
</html>
```